Long Established Local Fencing (not swords) Business needs fresh Business Cards

We need fresh double sided business cards for our Fencing Construction business, we are looking for something with our new logo design added, and maybe a photo background ?
We recently had cards made from Cardlyne and we were horrified with what we got back, the quality was terrible, so am looking for high quality format for good printing company to make.
We install Steelmora, Timber paling, Aluminium Slat Screening, Picket (timber and aluminium) and most other fencing installations.
Our website is brankelrails.com.au should you like to learn a bit more.
We do have logo in other formats if required.
We have been in business for over 35 years and we have used this as a "motto" it is on our signage

Industry/Entity Type

Construction

Contact Information for Business Card

Open to ideas, we need 3 x different cards, one generic with no name and 2 x others each with 1 of our bosses name on each, I will put into upload files.

Colors
ec1f27
000000
606060
f5f5f5

Requirements
Must have
• Company Name and Logo
• Address
• Contact details, phone, website, email etc
• Small space to write notes when leaving card at residence
Nice to have
• Our motto "Servicing the Peninsula for over 35 years"

```html
<!DOCTYPE html>
<html lang="en">
<head>
<meta charset="utf-8">
<title>Brankel Rails – Business Card</title>
<link href="https://fonts.googleapis.com/css2?family=Roboto:ital,wght@0,400;0,700;0,900;1,400&display=swap" rel="stylesheet">
<style>
  :root {
    --brand-red: #dc3232;
    --brand-black: #151515;
    --brand-grey: #606060;
    --card-white: #f5f5f5;
    --stage: #2b2b2b;
    --note-line: #555;
    --motto: #555;
  }
  html, body {
    margin: 0;
    width: 1200px;
    height: 960px;
    overflow: hidden;
    background: var(--stage);
    font-family: "Roboto", Arial, sans-serif;
  }
  .canvas { position: relative; width: 1200px; height: 960px; }
  .card {
    position: absolute;
    left: 313px;
    width: 600px;
    height: 342px;
    box-sizing: border-box;
  }
  .card-front { top: 113px; background: var(--brand-red); color: #fff; }
  .card-back { top: 472px; background: var(--card-white); }

  .front-brand {
    position: absolute;
    left: 40px;
    top: 130px;
    display: flex;
    align-items: center;
    gap: 12px;
    font-weight: 900;
    font-size: 34px;
    letter-spacing: 1px;
    color: #fff;
  }
  .front-brand .mark { width: 22px; height: 22px; background: #fff; }

  .contact-block {
    position: absolute;
    right: 29px;
    top: 146px;
    text-align: right;
  }
  .person-name { font-weight: 700; font-size: 20px; margin: 0 0 10px; line-height: 24px; }
  .details { font-size: 14px; line-height: 18px; margin: 0; }
  .contacts { list-style: none; margin: 12px 0 0; padding: 0; font-size: 14px; line-height: 19px; }
  .contacts li { display: flex; justify-content: flex-end; align-items: center; gap: 6px; }
  .contacts svg { width: 13px; height: 13px; fill: #fff; }

  .back-brand {
    position: absolute;
    top: 40px;
    left: 0; right: 0;
    display: flex;
    justify-content: center;
    align-items: center;
    gap: 10px;
    font-weight: 900;
    font-size: 26px;
    letter-spacing: 1px;
    color: var(--brand-black);
  }
  .back-brand .mark { width: 18px; height: 18px; background: var(--brand-red); }

  .note-lines { position: absolute; left: 48px; width: 500px; top: 129px; }
  .note-line { height: 0; border-bottom: 1px dotted var(--note-line); margin-bottom: 34px; }

  .motto {
    position: absolute;
    left: 0; right: 0;
    top: 302px;
    text-align: center;
    font-style: italic;
    font-size: 14px;
    color: var(--motto);
    margin: 0;
  }
</style>
</head>
<body>
<div class="canvas">
  <section class="card card-front">
    <div class="front-brand"><span class="mark"></span>BRANKEL RAILS</div>
    <div class="contact-block">
      <p class="person-name">DORIAN KESLEY</p>
      <p class="details">42 Tallow St Brankel<br>License No: 51724k<br>ABN 64 218 90 357</p>
      <ul class="contacts">
        <li>(02)49572186
          <svg viewBox="0 0 24 24"><path d="M6.6 10.8a15 15 0 0 0 6.6 6.6l2.2-2.2a1 1 0 0 1 1-.25 11 11 0 0 0 3.6.6 1 1 0 0 1 1 1V20a1 1 0 0 1-1 1A17 17 0 0 1 3 4a1 1 0 0 1 1-1h3.5a1 1 0 0 1 1 1 11 11 0 0 0 .6 3.6 1 1 0 0 1-.25 1z"/></svg></li>
        <li>0427 385 640
          <svg viewBox="0 0 24 24"><path d="M7 1h10a2 2 0 0 1 2 2v18a2 2 0 0 1-2 2H7a2 2 0 0 1-2-2V3a2 2 0 0 1 2-2zm0 3v14h10V4zm5 15.5a1 1 0 1 0 0 2 1 1 0 0 0 0-2z"/></svg></li>
        <li>brankelrails@mailpost.com
          <svg viewBox="0 0 24 24"><path d="M2 5h20v14H2zm2 2v.5l8 5 8-5V7z"/></svg></li>
        <li>www.brankelrails.com.au
          <svg viewBox="0 0 24 24"><path d="M12 2a10 10 0 1 0 0 20 10 10 0 0 0 0-20zm-1 17.9A8 8 0 0 1 4.1 11H7l4 4zM13 4.1a8 8 0 0 1 6.7 11.5L17 13h-3l-2-2 3-3V5z"/></svg></li>
      </ul>
    </div>
  </section>

  <section class="card card-back">
    <div class="back-brand"><span class="mark"></span>BRANKEL RAILS</div>
    <div class="note-lines">
      <div class="note-line"></div>
      <div class="note-line"></div>
      <div class="note-line"></div>
      <div class="note-line"></div>
      <div class="note-line"></div>
    </div>
    <p class="motto">Servicing the Peninsula for over 35 years</p>
  </section>
</div>
</body>
</html>
```